Niche Fitness Rebrand : Q7 Peak Conditioning

We're re-branding our fitness business and need to develop a cleaner, more sophisticated, and sleek website for our clients and potential clients to reference. We're looking to have some photo presence on all pages, with clean, crisp sections for easy reading on the web, and on mobile. We love the BVRdal(.com) website, which represents a very similar target market, and one of the same methods that our business represents. We're looking to take this local studio to a more professional level for future expansion, and need it to be sleek and in line with the growing and competitive marketplace for fitness.
Target Market(s)
70/30 women to men, physically active, upper middle class / professional between the ages of 28-42.
Industry/Entity Type
Fitness
Requirements
Must have
- sleek, professional, high-end design, with easy user navigation.
- About Page - with drop down child pages for management and coaches bios
- Classes Page 'The Methods' - with drop down child pages for different class types
- Location / Schedule Page
- Pricing
- Blog
- Private staff only programming login page
Nice to have
- potential to add an online retail shop -- but not currently necessary.
- Industry websites we like:
- www.bvrdal.example
- www.tarnbrookathletics.example

```html
<!DOCTYPE html>
<html lang="en">
<head>
<meta charset="utf-8">
<title>Q7 Peak Conditioning</title>
<link rel="stylesheet" href="https://fonts.googleapis.com/css2?family=Lato:wght@400;700&family=Open+Sans:wght@400;600&display=swap">
<style>
:root{
  --gold:#b49a6a;
  --ink:#222222;
  --muted:#555555;
  --white:#ffffff;
  --black:#0b0b0b;
}
*{margin:0;padding:0;box-sizing:border-box}
html,body{width:1200px;height:3557px;overflow:hidden;background:var(--white)}
body{position:relative;font-family:"Open Sans",Arial,sans-serif;color:var(--ink)}
.abs{position:absolute}
.heading{font-family:"Lato",Arial,sans-serif;font-weight:700;text-transform:uppercase;letter-spacing:.5px}

/* header */
.site-header{left:0;top:0;width:1200px;height:110px;background:var(--white)}
.brand-name{font-family:"Lato",Arial,sans-serif;font-weight:700;color:var(--ink);white-space:nowrap}
.site-header .brand-name{left:100px;top:40px;font-size:22px;line-height:28px}
.main-nav{right:100px;top:38px;display:flex;align-items:center;gap:24px;font-family:"Lato",Arial,sans-serif;font-size:14px;text-transform:uppercase;color:var(--ink)}
.login-btn{border:2px solid var(--gold);color:var(--gold);padding:7px 16px;display:flex;align-items:center;gap:6px}

/* hero */
.hero{left:0;top:110px;width:1200px;height:495px;background:linear-gradient(110deg,#2c2926 0%,#5d544b 45%,#8a7c6c 70%,#3d3732 100%)}
.hero-panel{left:225px;top:118px;width:747px;height:258px;background:rgba(255,255,255,.12)}
.hero-title{left:0;top:133px;width:1200px;text-align:center;color:var(--white);font-size:48px;font-weight:700;font-family:"Lato",Arial,sans-serif}
.hero-sub{left:0;top:198px;width:1200px;text-align:center;color:var(--white);font-size:22px}
.hero-text{left:340px;top:236px;width:520px;text-align:center;color:var(--white);font-size:13px;line-height:20px}
.btn-outline{border:2px solid rgba(255,255,255,.8);color:var(--white);font-family:"Lato",Arial,sans-serif;font-size:14px;text-transform:uppercase;display:flex;align-items:center;justify-content:center}
.hero-btn{left:538px;top:300px;width:124px;height:40px}
.hero-rule{left:0;top:600px;width:1200px;height:5px;background:var(--gold)}
.slider-tab{left:535px;top:565px;width:130px;height:65px;border-radius:65px 65px 0 0;background:var(--white);border:4px solid var(--gold);border-bottom:none;display:flex;justify-content:center;gap:8px;padding-top:30px}
.dot{width:12px;height:12px;border-radius:50%;border:2px solid var(--ink)}

/* section intro */
.section-title{left:0;width:1200px;text-align:center;font-size:28px;color:var(--ink)}
.section-intro{left:300px;width:600px;text-align:center;font-size:12.5px;line-height:24px;color:var(--muted)}

/* classes */
.class-card{top:821px;width:230px;height:194px;border:4px solid #eeeeee;overflow:hidden;background:var(--gold)}
.class-photo{left:0;top:0;width:222px;height:150px;border-radius:0 0 50% 50% / 0 0 40px 40px}
.class-label{left:0;top:152px;width:222px;text-align:center;color:var(--white);font-size:17px}

/* about */
.about{left:0;top:1105px;width:1200px;height:510px;background:linear-gradient(100deg,#2a2623 0%,#141312 40%,#1d1b19 70%,#34302c 100%)}
.about-frame{left:102px;top:74px;width:996px;height:365px;border:3px solid var(--gold)}
.about-title{left:0;top:118px;width:1200px;text-align:center;color:var(--white);font-size:30px}
.about-text{left:200px;top:190px;width:800px;text-align:center;color:var(--white);font-size:13px;line-height:21px}
.about-btn{left:536px;top:318px;width:128px;height:44px}
.about-arc{left:544px;top:390px;width:112px;height:56px;border:3px solid var(--gold);border-bottom:none;border-radius:56px 56px 0 0}

/* services */
.service{top:1830px;width:240px;text-align:center}
.service-icon{margin:0 auto;width:114px;height:114px;border-radius:50%;border:2px solid #e4e4e4;display:flex;align-items:center;justify-content:center}
.service-label{margin-top:26px;font-family:"Lato",Arial,sans-serif;font-size:17px;text-transform:uppercase;color:var(--ink)}

/* cardio video */
.cardio{left:0;top:2068px;width:1200px;height:465px;background:linear-gradient(100deg,#1a1816 0%,#3a332e 45%,#4d4139 60%,#151413 100%)}
.cardio-title{left:0;top:140px;width:1200px;text-align:center;color:var(--white);font-size:25px;line-height:44px}
.play-btn{left:567px;top:245px;width:66px;height:66px}

/* partners */
.partner{top:2630px;width:213px;height:110px;border:2px solid #e6e6e6;display:flex;align-items:center;justify-content:center;gap:10px;font-family:"Lato",Arial,sans-serif;font-size:20px;color:var(--ink)}
.partner-dot{width:18px;height:18px;border-radius:50%;background:var(--ink)}

/* map */
.map{left:0;top:2832px;width:1200px;height:306px;background:linear-gradient(135deg,#e9e6df 0%,#dcdfd6 45%,#e3e7ec 100%)}
.map-card{left:481px;top:90px;width:238px;height:62px;background:var(--white);box-shadow:0 1px 4px rgba(0,0,0,.2);text-align:center;font-size:13px;line-height:20px;padding-top:11px;color:var(--muted)}

/* footer */
.site-footer{left:0;top:3138px;width:1200px;height:419px;background:var(--black)}
.site-footer .brand-name{left:0;top:66px;width:1200px;text-align:center;color:var(--white);font-size:28px;line-height:34px}
.social{left:457px;top:175px;display:flex;gap:12px}
.social span{width:48px;height:48px;border-radius:50%;border:2px solid var(--gold)}
.footer-nav{left:0;width:1200px;display:flex;justify-content:center;gap:26px;color:var(--white);font-size:13px}
.footer-rule{left:100px;top:351px;width:1000px;height:1px;background:#555555}
.copyright{left:0;top:377px;width:1200px;text-align:center;color:#cccccc;font-size:12px}
</style>
</head>
<body>

<header class="abs site-header">
  <div class="abs brand-name">Q7 Peak Conditioning</div>
  <nav class="abs main-nav">
    <span>Home</span><span>About</span><span>Classes</span><span>Location</span><span>Pricing</span><span>Blog</span><span>Contact Us</span>
    <span class="login-btn"><svg width="10" height="12" viewBox="0 0 10 12"><rect x="1" y="5" width="8" height="7" fill="#b49a6a"/><path d="M2.5 5V3.5a2.5 2.5 0 0 1 5 0V5" stroke="#b49a6a" stroke-width="1.4" fill="none"/></svg>Login</span>
  </nav>
</header>

<section class="abs hero" role="img" aria-label="Photo of a man and a woman lifting barbells in a gym">
  <div class="abs hero-panel"></div>
  <h1 class="abs hero-title">PERFECT FITNESS</h1>
  <p class="abs hero-sub heading">Best choice for your fitness</p>
  <p class="abs hero-text">Contrary to popular belief, Lorem Ipsum is not simply random text. It has roots in a piece of classical Latin literature from 45 BC, making it over 2000 years old.</p>
  <span class="abs btn-outline hero-btn">Read More</span>
</section>
<div class="abs hero-rule"></div>
<div class="abs slider-tab"><span class="dot"></span><span class="dot"></span><span class="dot"></span></div>

<section class="classes">
  <h2 class="abs section-title heading" style="top:691px">Our Classes</h2>
  <p class="abs section-intro" style="top:733px">It is a long established fact that a reader will be distracted by the readable content of a page when looking at its layout. The point of using Lorem Ipsum is that it has a more-or-less</p>
  <div class="abs class-card" style="left:100px"><div class="abs class-photo" role="img" aria-label="Photo of a megaformer class" style="background:linear-gradient(160deg,#6b5a58,#3b3a4a)"></div><div class="abs class-label heading">Megaformer</div></div>
  <div class="abs class-card" style="left:357px"><div class="abs class-photo" role="img" aria-label="Photo of a rowing class" style="background:linear-gradient(160deg,#8b8478,#4c463f)"></div><div class="abs class-label heading">Rowing</div></div>
  <div class="abs class-card" style="left:614px"><div class="abs class-photo" role="img" aria-label="Photo of a core workout class" style="background:linear-gradient(160deg,#7c7067,#3c3530)"></div><div class="abs class-label heading">Core</div></div>
  <div class="abs class-card" style="left:871px"><div class="abs class-photo" role="img" aria-label="Photo of a boxing class" style="background:linear-gradient(160deg,#5e4b4f,#2f2a35)"></div><div class="abs class-label heading">Boxing</div></div>
</section>

<section class="abs about" role="img" aria-label="Photo of two athletes training with dumbbells">
  <div class="abs about-frame"></div>
  <h2 class="abs about-title heading">About Us</h2>
  <p class="abs about-text">There are many variations of passages of Lorem Ipsum available, but the majority have suffered alteration in some form, by injected humour, or randomised words which don't look even slightly believable. If you are going to use a passage of Lorem Ipsum, you need to be sure there isn't anything embarrassing hidden in the middle of text. All the Lorem Ipsum generators on the Internet tend to repeat predefined chunks as necessary.</p>
  <span class="abs btn-outline about-btn">Read More</span>
  <div class="abs about-arc"></div>
</section>

<section class="services">
  <h2 class="abs section-title heading" style="top:1695px">Our Services</h2>
  <p class="abs section-intro" style="top:1745px">It is a long established fact that a reader will be distracted by the readable content of a page when looking at its layout. The point of using Lorem Ipsum is that it has a more-or-less</p>
  <div class="abs service" style="left:46px"><div class="service-icon"><svg width="56" height="50" viewBox="0 0 56 50" fill="#b49a6a"><circle cx="28" cy="9" r="7"/><path d="M6 14c6 4 12 6 22 6s16-2 22-6l3 6c-6 5-11 7-16 8v20H19V28c-5-1-10-3-16-8z"/></svg></div><div class="service-label">Body Building</div></div>
  <div class="abs service" style="left:238px"><div class="service-icon"><svg width="56" height="50" viewBox="0 0 56 50" fill="none" stroke="#b49a6a" stroke-width="4"><circle cx="12" cy="38" r="9"/><circle cx="44" cy="38" r="9"/><path d="M12 38l12-16h14l6 16M24 22l8 16"/><circle cx="34" cy="8" r="5" fill="#b49a6a" stroke="none"/></svg></div><div class="service-label">Cycling</div></div>
  <div class="abs service" style="left:442px"><div class="service-icon"><svg width="56" height="50" viewBox="0 0 56 50" fill="#b49a6a"><circle cx="14" cy="10" r="6"/><path d="M10 18h8l4 14h22v6H18zM30 22l16-10 3 4-16 10z"/><rect x="4" y="44" width="48" height="4"/></svg></div><div class="service-label">Pilates Workout</div></div>
  <div class="abs service" style="left:679px"><div class="service-icon"><svg width="56" height="50" viewBox="0 0 56 50" fill="#b49a6a"><rect x="2" y="6" width="52" height="4"/><rect x="4" y="0" width="6" height="16"/><rect x="46" y="0" width="6" height="16"/><circle cx="28" cy="18" r="5"/><path d="M14 10h6l4 12h8l4-12h6l-6 18v20h-6V36h-4v12h-6V28z"/></svg></div><div class="service-label">Weight Lifting</div></div>
  <div class="abs service" style="left:907px"><div class="service-icon"><svg width="56" height="30" viewBox="0 0 56 30" fill="#b49a6a"><rect x="0" y="12" width="4" height="6"/><rect x="5" y="4" width="6" height="22"/><rect x="12" y="8" width="5" height="14"/><rect x="17" y="13" width="22" height="4"/><rect x="39" y="8" width="5" height="14"/><rect x="45" y="4" width="6" height="22"/><rect x="52" y="12" width="4" height="6"/></svg></div><div class="service-label">Power Training</div></div>
</section>

<section class="abs cardio" role="img" aria-label="Video still of a woman training on a rowing machine">
  <h2 class="abs cardio-title heading">Experience the most efficient cardio and<br>endurance training</h2>
  <svg class="abs play-btn" viewBox="0 0 66 66"><circle cx="33" cy="33" r="31" fill="none" stroke="#ffffff" stroke-width="3"/><path d="M26 20l20 13-20 13z" fill="#ffffff"/></svg>
</section>

<section class="partners">
  <div class="abs partner" style="left:100px"><span class="partner-dot"></span>Stonevale</div>
  <div class="abs partner" style="left:368px;font-size:18px">Kelvara Health</div>
  <div class="abs partner" style="left:624px;font-size:18px">Your Business</div>
  <div class="abs partner" style="left:887px">loremipsum</div>
</section>

<section class="abs map" role="img" aria-label="Street map showing the studio location">
  <div class="abs map-card">123 Sample Street, Sample City,<br>Sample State</div>
  <svg class="abs" style="left:586px;top:166px" width="24" height="34" viewBox="0 0 24 34"><path d="M12 0a12 12 0 0 0-12 12c0 9 12 22 12 22s12-13 12-22A12 12 0 0 0 12 0z" fill="#d32f2f"/><circle cx="12" cy="12" r="4.5" fill="#ffffff"/></svg>
</section>

<footer class="abs site-footer">
  <div class="abs brand-name">Q7 Peak Conditioning</div>
  <div class="abs social"><span></span><span></span><span></span><span></span><span></span></div>
  <nav class="abs footer-nav" style="top:262px"><span>Home</span><span>About</span><span>Classes</span><span>Location</span><span>Pricing</span><span>Blog</span><span>Contact us</span></nav>
  <nav class="abs footer-nav" style="top:296px"><span>Contact</span><span>Reviews</span><span>Hours</span><span>Help</span></nav>
  <div class="abs footer-rule"></div>
  <p class="abs copyright">© Copyright 2017 Q7 Peak Conditioning. All Rights Reserved</p>
</footer>

</body>
</html>
```